small business focused on life coaching and helping others "create better tomorrows" needs a website

The Pell R Group needs a website that focuses on life coaching and helping others "create better tomorrows"; This is a sole proprietorship so the focus should be on Marla, who has worn many hats and in an excellent position to help others. It should include 6 pages _ Home, Bio, Services, Book, Media, Contact Us and the logo that was created by Craft Plaza; also include testimonials from 5-6 individuals as well as why one might need these services (see file included)

Target Market(s)

Immigrants who need help navigating American system in the workplace, home or community, immigrant or at-risk students unable to communicate with their immigrant parents (due to language or unfamiliarity with the new culture) but would share with someone they trust, those in need of a mentor or help with career advancement or choices, those in need of help with public speaking or leadership development - Marla is someone who has worn many hats and in a position to help - extensive networking, an immigrant herself, former teacher, community leader, TV talk show host, author, mother, grandmother, etc.

Industry/Entity Type

Business

Coding

Coded - Design and coding required

Number of Pages Required

5+ page

Font styles to use
Sans Serif

Colors
cadf82
add136

Requirements
Must have
• visuals of Marla - present image of competency, caring, professionalism; need to include a 30-second video (in process of being produced) of Marla promoting the services, need to include 5-6 testimonials (which will be sent later). Please see the document that describes the different pages of the website and what should be included. Give the image of Marla's ability to help people GROW into a more productive self
Nice to have
• This is a sole proprietor business and as such, need to have people feel comfortable in who I am - trust is critical and that is why experience and competency should be shown

```html
<!DOCTYPE html>
<html lang="en">
<head>
<meta charset="utf-8">
<title>The Pell R Group – Create Better Tomorrows</title>
<link rel="stylesheet" href="https://fonts.googleapis.com/css2?family=Poppins:wght@300;400;500;600;700&display=swap">
<style>
:root{
  --green:#a6ce39;
  --green-light:#c6df84;
  --footer:#a8cf3e;
  --ink:#222;
  --text:#444;
  --grey-bg:#eeeeee;
  --white:#fff;
}
*{margin:0;padding:0;box-sizing:border-box}
html,body{width:1200px;height:3056px;overflow:hidden}
body{font-family:'Poppins',sans-serif;color:var(--text);background:var(--white);position:relative}
a{color:inherit;text-decoration:none}

/* header */
.site-header{position:absolute;left:0;top:0;width:1200px;height:160px;background:var(--white)}
.brand{position:absolute;left:163px;top:14px;width:220px;text-align:center}
.brand-mark{display:block;width:80px;height:80px;border:3px solid #333;border-radius:50%;margin:0 auto 8px}
.brand-name{font-size:23px;font-weight:500;color:#222;letter-spacing:.5px;white-space:nowrap}
.search{position:absolute;left:670px;top:39px;width:251px;height:38px;border:1px solid #bbb;border-radius:19px;font-size:13px;font-style:italic;color:#555;padding:9px 18px}
.search svg{position:absolute;right:14px;top:11px}
.login{position:absolute;left:929px;top:39px;width:110px;height:38px;border-radius:19px;background:var(--green);color:var(--white);font-size:14px;text-align:center;line-height:38px}
.main-nav{position:absolute;top:112px;left:0;width:1200px;font-size:16px;color:#222}
.main-nav a{position:absolute;white-space:nowrap}
.main-nav a.current{color:var(--green)}

/* hero */
.hero{position:absolute;left:0;top:160px;width:1200px;height:510px;background:linear-gradient(90deg,#0b0b0b 0%,#151515 45%,#3a2f2c 70%,#5a4a44 100%)}
.hero-photo{position:absolute;left:640px;top:0;width:560px;height:510px;background:radial-gradient(ellipse at 55% 55%,#6a5750 0%,#3b302d 55%,rgba(20,20,20,0) 85%)}
.hero-title{position:absolute;left:161px;top:112px;font-size:33px;font-weight:700;color:var(--green)}
.hero-list{position:absolute;left:161px;top:178px;list-style:none;font-size:12.6px;color:#e8e8e8;line-height:17px}
.hero-list li{position:relative;padding-left:20px;margin-bottom:11px;width:470px}
.hero-list li.wide{width:640px}
.hero-list li::before{content:"";position:absolute;left:0;top:3px;width:10px;height:10px;border:2px solid var(--green);border-radius:50%}
.slider-dots{position:absolute;left:512px;top:477px;display:flex;gap:4px}
.slider-dots span{width:41px;height:4px;background:#fff}
.slider-dots span.off{background:#999}

/* welcome */
.welcome{position:absolute;left:0;top:670px;width:1200px;height:463px;background:var(--grey-bg)}
.welcome-copy{position:absolute;left:161px;top:102px;width:440px}
.welcome h2{font-size:31px;font-weight:400;color:#222;line-height:44px;margin-bottom:10px}
.welcome p{font-size:10.6px;line-height:21px;color:#333}
.btn{display:block;background:var(--green);color:var(--white);font-size:12px;font-weight:600;text-align:center}
.welcome .btn{width:110px;height:39px;line-height:39px;margin-top:20px}
.welcome-photo{position:absolute;left:664px;top:55px;width:373px;height:351px;background:linear-gradient(160deg,#6d5a44 0%,#4a3a2e 45%,#b28c66 80%,#8a6a4e 100%)}

/* services */
.services-intro{position:absolute;left:0;top:1188px;width:1200px;text-align:center}
.services-intro h2{font-size:31px;font-weight:400;color:#222}
.services-intro p{width:700px;margin:12px auto 0;font-size:10.4px;line-height:22px;color:#444}
.tile{position:absolute;top:1314px;height:393px;color:var(--white)}
.tile-title{position:absolute;left:0;width:100%;top:166px;text-align:center;font-size:18px;font-weight:600}
.tile-more{position:absolute;left:0;width:100%;top:204px;text-align:center;font-size:12px}
.tile-more svg{vertical-align:middle;margin-left:6px}
.tile::after{content:"";position:absolute;left:50%;bottom:0;margin-left:-20px;border-left:20px solid transparent;border-right:20px solid transparent;border-bottom:16px solid var(--green)}
.t-careers{left:0;width:293px;background:linear-gradient(135deg,#4a4f55,#23282d)}
.t-accult{left:301px;width:294px;background:linear-gradient(180deg,#6b7066,#2f3530 60%,#4b4a42)}
.t-leader{left:603px;width:293px;background:linear-gradient(135deg,#7d8185,#4f5458)}
.t-speak{left:904px;width:296px;background:linear-gradient(135deg,#5a3430,#2a2224 60%,#3a2b2a)}
.mini-dots{position:absolute;left:582px;top:1737px;display:flex;gap:3px}
.mini-dots span{width:9px;height:9px;border-radius:50%;background:#aaa}
.mini-dots span.on{background:var(--green)}

/* testimonials */
.testimonials{position:absolute;left:0;top:1762px;width:1200px;height:485px;background:var(--grey-bg)}
.notch{position:absolute;left:570px;top:0;border-left:30px solid transparent;border-right:30px solid transparent;border-top:22px solid var(--white)}
.testimonials h2{position:absolute;left:0;width:1200px;top:66px;text-align:center;font-size:31px;font-weight:400;color:#222}
.quote{position:absolute;top:140px;width:418px}
.quote-mark{font-size:52px;font-weight:700;color:var(--green);line-height:40px;height:34px}
.quote p{font-size:11.6px;line-height:24.8px;color:#333}
.quote-name{margin-top:14px;font-size:16px;font-weight:700;color:var(--green)}
.q-left{left:161px}
.q-right{left:625px}
.divider{position:absolute;left:597px;top:140px;width:1px;height:300px;background:#ccc}
.arrow{position:absolute;top:258px}

/* video */
.video h2{position:absolute;left:161px;top:2340px;font-size:31px;font-weight:400;color:#222}
.video p{position:absolute;left:161px;top:2393px;width:340px;font-size:10.6px;line-height:21.6px;color:#333}
.video-frame{position:absolute;left:550px;top:2314px;width:487px;height:306px;background:linear-gradient(135deg,#6b3a2a 0%,#3b2420 50%,#7a5a3e 100%)}
.video-frame svg{position:absolute;left:206px;top:117px}

/* signup */
.signup{position:absolute;left:0;top:2689px;width:1200px;height:94px;background:var(--green-light)}
.signup h3{position:absolute;left:161px;top:32px;font-size:20px;font-weight:400;color:var(--white)}
.signup .field{position:absolute;left:554px;top:32px;width:395px;height:41px;background:var(--white);font-size:11px;color:#888;padding:13px 12px}
.signup .btn{position:absolute;left:949px;top:32px;width:90px;height:41px;line-height:41px}

/* footer */
.site-footer{position:absolute;left:0;top:2783px;width:1200px;height:273px;background:var(--footer);color:var(--white)}
.footer-brand{position:absolute;left:163px;top:26px;width:220px;text-align:center}
.footer-brand .brand-mark{border-color:var(--white)}
.footer-brand .brand-name{color:var(--white)}
.f-col{position:absolute;top:28px;font-size:12px;line-height:22.4px}
.f-col h4{font-size:17px;font-weight:600;margin-bottom:8px}
.f-col ul{list-style:none}
.f-contact li{position:relative;padding-left:26px}
.f-contact svg{position:absolute;left:0;top:6px}
.footer-rule{position:absolute;left:161px;top:211px;width:878px;height:1px;background:rgba(255,255,255,.55)}
.copyright{position:absolute;left:161px;top:230px;font-size:11.5px}
.social{position:absolute;left:933px;top:231px;display:flex;gap:14px}
.social span{width:13px;height:13px;border-radius:50%;background:var(--white)}
</style>
</head>
<body>

<header class="site-header">
  <div class="brand"><span class="brand-mark"></span><div class="brand-name">The Pell R Group</div></div>
  <div class="search">Search
    <svg width="14" height="14" viewBox="0 0 14 14"><circle cx="6" cy="6" r="4.5" fill="none" stroke="#333" stroke-width="2"/><line x1="9.3" y1="9.3" x2="13" y2="13" stroke="#333" stroke-width="2"/></svg>
  </div>
  <a class="login" href="#">Login</a>
  <nav class="main-nav">
    <a class="current" style="left:543px" href="#">Home</a>
    <a style="left:627px" href="#">Bio</a>
    <a style="left:690px" href="#">Services</a>
    <a style="left:790px" href="#">Book</a>
    <a style="left:866px" href="#">Media</a>
    <a style="left:954px" href="#">Contact Us</a>
  </nav>
</header>

<section class="hero">
  <div class="hero-photo" role="img" aria-label="Group photo of Marla with family members seated together"></div>
  <h1 class="hero-title">Create Better Tomorrows</h1>
  <ul class="hero-list">
    <li class="wide">Are you an immigrant needing help navigating the American system?</li>
    <li>Are you an immigrant parent unable to support your children's career choice or life issue</li>
    <li class="wide">Do you need help with your job search?</li>
    <li class="wide">Are you considering a career change?</li>
    <li class="wide">Are you struggling to balance demands of work, home and life?</li>
    <li class="wide">Do you need help with time management, leadership development, etc.?</li>
    <li class="wide">Are you worried about your teenager's change in behavior?</li>
    <li class="wide">Is your family struggling with an addiction/mental health issue?</li>
  </ul>
  <div class="slider-dots"><span></span><span></span><span class="off"></span><span></span></div>
</section>

<section class="welcome">
  <div class="welcome-copy">
    <h2>Welcome to Pell R group</h2>
    <p>Marla is a creative, results oriented leader with exceptional people and communication skills, multicultural perspectives and half a century of experience motivating people to action. In communities where she has lived and worked, Marla is known, loved and respected. She successfully balances multiple roles as an accomplished woman in the workplace, in the community and in the home. For decades, Marla has helped immigrants navigate a system foreign to them and helped their children bridge multiple gaps. She has assisted women with life's challenges and supported their empowerment.</p>
    <a class="btn" href="#">READ MORE</a>
  </div>
  <div class="welcome-photo" role="img" aria-label="Marla standing with a guest at a kitchen counter"></div>
</section>

<section class="services">
  <div class="services-intro">
    <h2>Nature of business and Special Areas</h2>
    <p>Sed ut perspiciatis unde omnis iste natus sitolu ptatem accusantium doloremque lantium, totme maperiam, eaque ipsa quae ab illo inventore veritati quasi archite ed ut perspiciatis unde omnis iste natus sitolu ptatem accusantium doloremque</p>
  </div>
  <div class="tile t-careers" role="img" aria-label="Photo of a young professional at a desk">
    <div class="tile-title">Careers</div>
    <div class="tile-more">Learn More<svg width="22" height="22" viewBox="0 0 22 22"><circle cx="11" cy="11" r="9.5" fill="none" stroke="#fff" stroke-width="1.5"/><path d="M9 7l4 4-4 4" fill="none" stroke="#fff" stroke-width="1.5"/></svg></div>
  </div>
  <div class="tile t-accult" role="img" aria-label="Photo of a traditional pavilion and bridge">
    <div class="tile-title">Acculturation</div>
    <div class="tile-more">Learn More<svg width="22" height="22" viewBox="0 0 22 22"><circle cx="11" cy="11" r="9.5" fill="none" stroke="#fff" stroke-width="1.5"/><path d="M9 7l4 4-4 4" fill="none" stroke="#fff" stroke-width="1.5"/></svg></div>
  </div>
  <div class="tile t-leader" role="img" aria-label="Photo of a presenter leading a meeting">
    <div class="tile-title">Leadership Development</div>
    <div class="tile-more">Learn More<svg width="22" height="22" viewBox="0 0 22 22"><circle cx="11" cy="11" r="9.5" fill="none" stroke="#fff" stroke-width="1.5"/><path d="M9 7l4 4-4 4" fill="none" stroke="#fff" stroke-width="1.5"/></svg></div>
  </div>
  <div class="tile t-speak" role="img" aria-label="Photo of a speaker addressing an audience">
    <div class="tile-title">Public Speaking</div>
    <div class="tile-more">Learn More<svg width="22" height="22" viewBox="0 0 22 22"><circle cx="11" cy="11" r="9.5" fill="none" stroke="#fff" stroke-width="1.5"/><path d="M9 7l4 4-4 4" fill="none" stroke="#fff" stroke-width="1.5"/></svg></div>
  </div>
  <div class="mini-dots"><span class="on"></span><span></span><span></span></div>
</section>

<section class="testimonials">
  <div class="notch"></div>
  <h2>Testimonials</h2>
  <svg class="arrow" style="left:86px" width="16" height="26" viewBox="0 0 16 26"><path d="M13 2L3 13l10 11" fill="none" stroke="#999" stroke-width="2"/></svg>
  <svg class="arrow" style="left:1114px" width="16" height="26" viewBox="0 0 16 26"><path d="M3 2l10 11L3 24" fill="none" stroke="#999" stroke-width="2"/></svg>
  <div class="quote q-left">
    <div class="quote-mark">“</div>
    <p>Marla is my "go-to" person for just about anything. she has been a significant support in my acculturation into western/western culture – helping me navigate the many aspects of life's journey. through her guidance, I have gained much confidence in myself and in my approach to resolving issues. her immigrant experience helps her understand my challenges. her decades of living and working in this country enables her to provide advice based on personal experience. i cannot thank her enough for always being there whenever i have needed guidance.</p>
    <div class="quote-name">-NADIA K</div>
  </div>
  <div class="divider"></div>
  <div class="quote q-right">
    <div class="quote-mark">“</div>
    <p>Thank you to ms. marla for helping me with getting a good job with benefits – and then being promoted from that job two years later. i met ms. marla while painting her house. since then, she has gone out of her way to help me write a resume, apply for jobs and interview for my first job with the county school system. whenever i have a question about anything, i know i can call her and she gets right back to me. I am very lucky to have someone like her take the time to watch over me.</p>
    <div class="quote-name">-LUIS M</div>
  </div>
</section>

<section class="video">
  <h2>Our Video</h2>
  <p>Sed ut perspiciatis unde omnis iste natus error sit voluptatem accusantium doloremque laudantium, totam rem aperiam, eaq ue ipsa quae ab illo inventore veritatis et quasi architecto beatae vitae dicta sunt explicabo. Nemo enim ipsam voluptatem quia voluptas sit aspernatur aut odit aut fugit, sed quia consequuntur magni dolores eos qui ratione voluptatem sequi nesciunt. Neue porro quisquam est, qui dolorem ipsum quia dolor sit amet, consectetur, adipisci velit, sed quia non numquam eius modi tempora incidunt ut labore et dolore magna.</p>
  <div class="video-frame" role="img" aria-label="Video still of Marla speaking at a podium">
    <svg width="76" height="76" viewBox="0 0 76 76"><circle cx="38" cy="38" r="36" fill="#fff"/><circle cx="38" cy="38" r="29" fill="#a6ce39"/><path d="M31 25l20 13-20 13z" fill="#fff"/></svg>
  </div>
</section>

<section class="signup">
  <h3>Sign up for the Latest News and Offers</h3>
  <div class="field">Enter Email Address</div>
  <a class="btn" href="#">SIGN UP</a>
</section>

<footer class="site-footer">
  <div class="footer-brand"><span class="brand-mark"></span><div class="brand-name">The Pell R Group</div></div>
  <div class="f-col" style="left:454px">
    <h4>Services</h4>
    <ul><li>Life coaching</li><li>Acculturation</li><li>Intergenerational Relations</li><li>Leadership development</li><li>Organizational management</li></ul>
  </div>
  <div class="f-col" style="left:723px">
    <h4>Help</h4>
    <ul><li>Home</li><li>Bio</li><li>Services</li><li>Book</li><li>Media</li></ul>
  </div>
  <div class="f-col f-contact" style="left:862px">
    <h4>Contact us</h4>
    <ul>
      <li><svg width="10" height="13" viewBox="0 0 10 13"><path d="M5 0a5 5 0 0 1 5 5c0 3-5 8-5 8S0 8 0 5a5 5 0 0 1 5-5z" fill="#fff"/><circle cx="5" cy="5" r="1.8" fill="#a8cf3e"/></svg>Marla Vance<br>4127 Cedar Hollow Lane<br>Brookfield, Maryland 20990</li>
      <li><svg width="12" height="9" viewBox="0 0 12 9"><rect width="12" height="9" fill="#fff"/><path d="M0 0l6 5 6-5" fill="none" stroke="#a8cf3e" stroke-width="1.2"/></svg>marla.vance@example.net</li>
      <li><svg width="11" height="11" viewBox="0 0 11 11"><path d="M2 0l2 3-1 1.5c.8 1.5 2 2.7 3.5 3.5L8 7l3 2-1.5 2C4.5 11 0 6.5 0 1.5z" fill="#fff"/></svg>Tel: 555-014-2290</li>
    </ul>
  </div>
  <div class="footer-rule"></div>
  <div class="copyright">© 2017 The Pell R group. All Copyrights are Reserved. Terms of Use</div>
  <div class="social" aria-label="Social links"><span></span><span></span><span></span><span></span></div>
</footer>

</body>
</html>
```